Brochure and Business Card design

I am looking for a high end, elegant A4, 4 page brochure booklet to convey our products to clientele that will be visiting a luxury display showroom.

Harbourline Guard and Grilles is a Australian security provider, and we supply high end products from reputable brands.
The brochure will be directed to clients building a new home with a partnered building company and will be accompanied with display boards of our products.

I am providing files of a document we have put together with the relevant information and some images to help along the way, we are not bound by the layout or style it has been drawn up and we wish to give you complete creative freedom putting the peaces together. I have also provided the files for our logo in two different colours, and a picture of a brochure we love the look of.

If you have any suggestions, we can likely come up with further images etc if it will help or even if you feel some should be removed, we are open to that also

Target Market(s)

Young familys, people building new luxury homes, proffesionals, home owners

Industry/Entity Type

Business

Font styles to use
Serif
Sans Serif

Requirements
Must have
• All 8 pages
Should not have
• Not really a fan of reds and similar.

```html
<!DOCTYPE html>
<html lang="en">
<head>
<meta charset="utf-8">
<title>Harbourline Guard and Grilles – Brochure Spread</title>
<link href="https://fonts.googleapis.com/css2?family=Open+Sans:wght@400;600;700&display=swap" rel="stylesheet">
<style>
  :root{
    --bg:#e9ebee;
    --paper:#f7f8fb;
    --blue:#2f6fc0;
    --blue-dark:#1f5aa8;
    --green:#8cc63f;
    --ink:#1d2433;
    --label:#3a6fb5;
    --label-bg:#eef2f8;
    --tile-border:#a9cf5a;
    --photo-border:#4a86cf;
    --deco-blue:#dbe8f6;
    --deco-green:#e7f0d6;
  }
  *{box-sizing:border-box;margin:0;padding:0}
  html,body{width:1200px;height:789px;overflow:hidden;background:var(--bg);
    font-family:"Open Sans",Arial,sans-serif;color:var(--ink)}
  .spread{position:absolute;left:77px;top:24px;width:1046px;height:740px;display:flex;
    box-shadow:0 6px 22px rgba(0,0,0,.18)}
  .page{position:relative;width:523px;height:740px;background:var(--paper);overflow:hidden}
  .page--left{border-right:1px solid #dfe3ea}
  .deco{position:absolute;inset:0;width:100%;height:100%}
  .band{position:absolute;height:24px;background:var(--blue);color:#fff;font-size:13px;
    line-height:24px;padding-left:22px;font-weight:400}
  .band::after{content:"";position:absolute;right:-16px;top:0;width:10px;height:24px;
    background:var(--green);transform:skewX(-20deg)}
  .copy{position:absolute;font-size:8.6px;line-height:1.45}
  .copy p+p{margin-top:6px}
  .photo{position:absolute;background:#fff;border:2px solid var(--photo-border);padding:6px}
  .photo__fill{width:100%;height:100%;background:linear-gradient(135deg,#e4e7ec,#a9b0bb)}
  .tile{position:absolute;width:104px}
  .tile__img{height:74px;background:#fff;border:2px solid var(--tile-border);padding:6px}
  .tile__img div{width:100%;height:100%;background:linear-gradient(135deg,#eef0f3,#b5bcc6)}
  .tile__label{margin-top:8px;background:var(--label-bg);border:1px solid #dde4ee;color:var(--label);
    font-size:8px;font-weight:600;text-align:center;line-height:1.25;padding:4px 3px}
</style>
</head>
<body>
<main class="spread">

  <section class="page page--left">
    <svg class="deco" viewBox="0 0 523 740" aria-hidden="true">
      <circle cx="560" cy="480" r="300" fill="var(--deco-blue)" opacity=".55"/>
      <circle cx="560" cy="560" r="200" fill="var(--deco-green)" opacity=".7"/>
    </svg>

    <h2 class="band" style="left:40px;top:40px;width:210px">Alarm Systems</h2>
    <div class="copy" style="left:60px;top:76px;width:420px">
      <p>A Harbourline Guard and Grilles alarm system with its state of the art equipment is the perfect defense for your family and home. With detection devices such as motion detectors, magnetic door sensors and warning devices like siren + strobe combos to alert others of a break in to name a few, it will be everything you need to feel secure.</p>
      <p>With the added option of having your security system monitored, you will always have someone watching over your home, even when even when the house is vacant.</p>
      <p>Did you know, industry leaders say that burglars are 3 times more likely to target a home without a security system. This means that simply having a home security system always keeps you safer, even if an alarm is never triggered.</p>
    </div>

    <h2 class="band" style="left:40px;top:212px;width:190px">Home Kits</h2>
    <div class="copy" style="left:60px;top:248px;width:250px">
      <p>Standard kits consisting of everything you need to get an alarm up and running. Components such as an Alarm Control Panel, Keypad, 3 motion detectors, and internal siren, an external siren+strobe combo, battery back up incase the power goes out. A great starting platform that can be built on to your needs and requirements.</p>
      <p>Request a Security Advisor consultation for all the info.</p>
    </div>
    <div class="photo" style="left:330px;top:238px;width:150px;height:108px">
      <div class="photo__fill" role="img" aria-label="Alarm home kit: control panel, keypad, motion detectors and siren"></div>
    </div>

    <h2 class="band" style="left:40px;top:362px;width:220px">Popular Upgrades</h2>

    <div class="tile" style="left:40px;top:404px"><div class="tile__img"><div role="img" aria-label="OLED keypad"></div></div><p class="tile__label">OLED Keypad upgrade</p></div>
    <div class="tile" style="left:156px;top:404px"><div class="tile__img"><div role="img" aria-label="Remote fob and receiver board"></div></div><p class="tile__label">Remote Arm and Disarm</p></div>
    <div class="tile" style="left:272px;top:404px"><div class="tile__img"><div role="img" aria-label="Monitoring communicator with antenna"></div></div><p class="tile__label">Professional Alarm Monitoring</p></div>
    <div class="tile" style="left:388px;top:404px"><div class="tile__img"><div role="img" aria-label="Motion detector"></div></div><p class="tile__label">Motion Detectors in additional rooms</p></div>

    <div class="tile" style="left:80px;top:548px"><div class="tile__img"><div role="img" aria-label="Ceiling mounted 360 degree motion detector"></div></div><p class="tile__label">360 degree motion detectors</p></div>
    <div class="tile" style="left:210px;top:548px"><div class="tile__img"><div role="img" aria-label="Door and window magnetic reed switch"></div></div><p class="tile__label">Door and window magnetic switches</p></div>
    <div class="tile" style="left:340px;top:548px"><div class="tile__img"><div role="img" aria-label="Roller door magnetic switch"></div></div><p class="tile__label">Roller door magnetic switch</p></div>
  </section>

  <section class="page page--right">
    <svg class="deco" viewBox="0 0 523 740" aria-hidden="true">
      <circle cx="-40" cy="480" r="300" fill="var(--deco-blue)" opacity=".55"/>
      <circle cx="-40" cy="560" r="200" fill="var(--deco-green)" opacity=".7"/>
      <circle cx="600" cy="300" r="200" fill="var(--deco-blue)" opacity=".45"/>
    </svg>

    <h2 class="band" style="left:40px;top:40px;width:200px">Intercom</h2>
    <div class="copy" style="left:60px;top:76px;width:420px">
      <p>A Harbourline Guard and Grilles Intercom system is a great addition to any home. Giving you the ability to communicate with visitors to your home at your front door or even at your front gate. In conjunction with the use of an electric strike you can hit the door release button on the intercom and let them in from where you stand in the home. Maybe even better still decide to not let them in.</p>
      <p>With the video intercom option your visitor will be displayed automatically and you can view who it is without them even knowing you are there.</p>
    </div>

    <h2 class="band" style="left:40px;top:178px;width:210px">KL Colour Video Intercom</h2>
    <div class="copy" style="left:60px;top:212px;width:290px">
      <p>Superior quality, touch button control and door release. This sleek glass face 7" screen intercom is just what you need to visually see and communicate with who is at the front gate or door. With the add on addition of a extra monitor makes it perfect for two story homes with the extra station up stairs.</p>
    </div>

    <h2 class="band" style="left:40px;top:290px;width:210px">KM Colour Video Intercom</h2>
    <div class="copy" style="left:60px;top:324px;width:290px">
      <p>All the smarts built into a compact, modern designed glass face monitor. This unit has touch screen control, inter home communication between monitors and a build in handset for minimal disturbance when required. With maximums of 4 door stations and 8 Monitors, this system is perfect for the homes with multiple entry points and when multiple room monitors are required.</p>
    </div>

    <h2 class="band" style="left:40px;top:412px;width:210px">Audio Only Intercom</h2>
    <div class="copy" style="left:60px;top:446px;width:290px">
      <p>Whether it's to help fit within the budget, and you just don't have the requirement of having to see who is at the door, this no fuss, single purpose audio only intercom is that handy addition to the living area.</p>
    </div>

    <div class="photo" style="left:372px;top:210px;width:116px;height:92px"><div class="photo__fill" role="img" aria-label="Video intercom monitor with door station"></div></div>
    <div class="photo" style="left:372px;top:318px;width:116px;height:92px"><div class="photo__fill" role="img" aria-label="Compact video monitor with door station"></div></div>
    <div class="photo" style="left:372px;top:426px;width:116px;height:92px"><div class="photo__fill" role="img" aria-label="Audio door station and handset"></div></div>

    <h2 class="band" style="left:40px;top:534px;width:220px">Popular Upgrades</h2>

    <div class="tile" style="left:60px;top:578px"><div class="tile__img"><div role="img" aria-label="Flush mount stainless steel door station"></div></div><p class="tile__label">Upgrade to flush mount stainless steel door station</p></div>
    <div class="tile" style="left:210px;top:578px"><div class="tile__img"><div role="img" aria-label="Electric strike"></div></div><p class="tile__label">Extend intercom wiring to property font gate</p></div>
    <div class="tile" style="left:360px;top:578px"><div class="tile__img"><div role="img" aria-label="Additional video monitor"></div></div><p class="tile__label">Additional monitor installed. (Video Only)</p></div>
  </section>

</main>
</body>
</html>
```